Business Card Design Project

Hi,
I am after a business card design for a new business. The business is called Quarrel Works and is a stockist of building supplies used for modern cosmetic renovations for houses. (e.g Floorboards, timber decking, modern fittings and fixtures.)
The logo and font faces have been attached.
The logo comes in 2 different color scheme's - 1. Orange on White & 2. Orange on Black. I would like 2 versions of the business card design to reflect these color scheme's.
The designs need to be double sided. The front should contain all the contact information, whilst the back of the card should display the logo and the URL of the webpage - www.quarrelworks-demo.com.au . The logo needs to be displayed creatively on the back of the card.
The business card design needs to reflect the image of modern living, but should also have the wow factor.

```html
<!DOCTYPE html>
<html lang="en">
<head>
<meta charset="utf-8">
<title>Quarrel Works – Business Card</title>
<link rel="stylesheet" href="https://fonts.googleapis.com/css2?family=Roboto:wght@300;400&display=swap">
<style>
  :root {
    --backdrop: #e4e4e4;
    --card: #f3f3f3;
    --orange-light: #f47b2c;
    --orange-dark: #e4601b;
    --brand: #ee6e24;
    --ink: #222222;
    --ink-soft: #333333;
  }
  * { margin: 0; padding: 0; box-sizing: border-box; }
  html, body {
    width: 1200px; height: 353px; overflow: hidden;
    background: var(--backdrop);
    font-family: "Roboto", Arial, sans-serif;
  }
  .sheet { position: relative; width: 1200px; height: 353px; }
  .card {
    position: absolute; top: 24px;
    width: 576px; height: 305px;
    background: var(--card);
    border-radius: 24px 5px 24px 5px;
    overflow: hidden;
    box-shadow: 0 2px 6px rgba(0,0,0,0.18);
  }
  .card--front { left: 12px; }
  .card--back { left: 612px; }
  .card__accents { position: absolute; inset: 0; width: 100%; height: 100%; }

  .wordmark {
    position: absolute; display: flex; align-items: center;
    color: var(--brand); font-weight: 400; white-space: nowrap;
  }
  .wordmark__square { background: var(--brand); flex: none; }
  .wordmark--small { left: 42px; top: 38px; font-size: 20px; gap: 8px; }
  .wordmark--small .wordmark__square { width: 22px; height: 22px; }
  .wordmark--large {
    left: 0; right: 0; top: 116px; justify-content: center;
    font-size: 44px; gap: 14px;
  }
  .wordmark--large .wordmark__square { width: 52px; height: 52px; }

  .person { position: absolute; left: 296px; top: 106px; }
  .person__name {
    font-size: 28px; font-weight: 300; color: var(--ink); line-height: 30px;
  }
  .person__role {
    font-size: 13px; font-weight: 300; color: var(--ink-soft);
    letter-spacing: 1.5px; margin-left: 54px; line-height: 16px;
  }
  .contact {
    position: absolute; right: 49px; top: 176px;
    list-style: none; text-align: right;
    font-size: 14px; font-weight: 300; color: var(--ink); line-height: 20.5px;
  }
  .site-url {
    position: absolute; left: 0; right: 0; top: 189px; text-align: center;
    font-size: 18px; font-weight: 400; color: var(--ink-soft);
  }
</style>
</head>
<body>
<main class="sheet">
  <section class="card card--front">
    <svg class="card__accents" viewBox="0 0 576 305" aria-hidden="true">
      <defs>
        <linearGradient id="orangeFront" x1="0" y1="0" x2="1" y2="1">
          <stop offset="0" stop-color="var(--orange-light)"/>
          <stop offset="1" stop-color="var(--orange-dark)"/>
        </linearGradient>
      </defs>
      <polygon points="414,0 576,0 576,86" fill="url(#orangeFront)"/>
      <polygon points="0,164 0,305 180,305" fill="url(#orangeFront)"/>
    </svg>
    <div class="wordmark wordmark--small"><span class="wordmark__square"></span>Quarrel Works</div>
    <div class="person">
      <p class="person__name">Full Name</p>
      <p class="person__role">Manager</p>
    </div>
    <ul class="contact">
      <li>0 00 12 34 56</li>
      <li>yourname@quarrelworks-demo.com</li>
      <li>Quarrel Works oy</li>
      <li>Northfield, USA</li>
      <li>www.quarrelworks-demo.com</li>
    </ul>
  </section>

  <section class="card card--back">
    <svg class="card__accents" viewBox="0 0 576 305" aria-hidden="true">
      <defs>
        <linearGradient id="orangeBack" x1="0" y1="0" x2="1" y2="1">
          <stop offset="0" stop-color="var(--orange-light)"/>
          <stop offset="1" stop-color="var(--orange-dark)"/>
        </linearGradient>
      </defs>
      <polygon points="420,0 576,0 576,86" fill="url(#orangeBack)"/>
      <polygon points="0,164 0,305 162,305" fill="url(#orangeBack)"/>
    </svg>
    <div class="wordmark wordmark--large"><span class="wordmark__square"></span>Quarrel Works</div>
    <p class="site-url">www.quarrelworks-demo.com.au</p>
  </section>
</main>
</body>
</html>
```